Flyer for Home Improvement Lead Generation

We need a flyer that shows people the work we do. Replacement windows doors and siding. We offer quality products and great workmanship at fair prices. The company name is Granite Ridge Remodeling. I will upload a document with some of the features we would like to show in the flyer.
Wow would like to keep a homegrown look to our marketing.
We use Georgia font in caps for our logo text.
The hex for the logo color is #F67B04
This flyer will be for lead generation so it should showcase reasons to call us.
Our web address. grr-vt.com
Our Phone number. 860-412-9368
leave a spot for a QR code.
Target Market(s)
Residential
Industry/Entity Type
Home Improvement. Replacement windows, doors and siding
Look and feel

```html
<!DOCTYPE html>
<html lang="en">
<head>
<meta charset="utf-8">
<title>Granite Ridge Remodeling – Flyer</title>
<link href="https://fonts.googleapis.com/css2?family=Poppins:wght@400;500;600;700&family=Source+Serif+4:opsz,wght@8..60,400;8..60,600;8..60,700&display=swap" rel="stylesheet">
<style>
  :root {
    --backdrop: #8ea3a2;
    --ink: #0b0b0b;
    --paper: #ececec;
    --white: #ffffff;
    --brand-orange: #F67B04;
    --accent-orange: #e3821c;
    --gold: #f0a32a;
    --text-dark: #151515;
    --serif: "Source Serif 4", Georgia, serif;
    --sans: "Poppins", Arial, sans-serif;
  }
  * { margin: 0; padding: 0; box-sizing: border-box; }
  html, body { width: 1200px; height: 1117px; overflow: hidden; }
  body { background: var(--backdrop); position: relative; font-family: var(--sans); }

  .flyer {
    position: absolute; left: 220px; top: 20px;
    width: 760px; height: 1077px;
    background: var(--paper); overflow: hidden;
  }
  .abs { position: absolute; }

  /* top left hero */
  .hero-panel {
    left: 0; top: 0; width: 380px; height: 441px;
    background: linear-gradient(180deg, #141414 0%, #2b2b2b 55%, #3a3a3a 100%);
  }
  .side-strip { left: 0; top: 441px; width: 49px; height: 104px; background: #3a3a3a; }
  .brand-block {
    left: 65px; top: 0; width: 269px; height: 218px; background: var(--ink);
    display: flex; align-items: flex-end; justify-content: center; padding-bottom: 14px;
  }
  .brand-name {
    font-family: var(--serif); font-weight: 400; color: var(--brand-orange);
    font-size: 28px; line-height: 35px; text-align: center; letter-spacing: 0.5px;
    text-transform: uppercase;
  }
  .brand-divider { left: 58px; top: 228px; width: 298px; height: 1px; background: #777; }
  .headline {
    left: 58px; top: 242px; width: 320px;
    font-family: var(--serif); font-weight: 700; font-size: 33.5px; line-height: 35px;
    color: var(--white); text-transform: uppercase; letter-spacing: -0.2px;
  }
  .headline .highlight { color: var(--gold); }

  .hero-photo {
    left: 380px; top: 0; width: 380px; height: 441px;
    background: linear-gradient(160deg, #2f5fb5 0%, #5d84c7 22%, #e6e9e6 32%, #8e9c7c 48%, #7a8b69 75%, #6d7b5e 100%);
  }

  /* left white section */
  .home-photo {
    left: 58px; top: 450px; width: 322px; height: 192px;
    background: linear-gradient(180deg, #8fb1d9 0%, #c7d6e6 30%, #4e5458 55%, #3e4a3a 80%, #4f7a3a 100%);
  }
  .why-title {
    left: 58px; top: 664px; font-family: var(--serif); font-weight: 700;
    font-size: 28px; color: var(--text-dark);
  }
  .why-rule { left: 58px; top: 708px; width: 93px; height: 3px; background: var(--accent-orange); }
  .benefits { left: 58px; top: 728px; list-style: none; }
  .benefits li {
    display: flex; align-items: center; gap: 12px; height: 32px;
    font-weight: 700; font-size: 18px; color: var(--text-dark);
  }
  .benefits svg { width: 17px; height: 17px; flex: none; }

  /* contact band */
  .contact-band { left: 0; top: 872px; width: 380px; height: 188px; background: var(--ink); }
  .contact-title {
    left: 58px; top: 886px; font-family: var(--serif); font-weight: 700;
    font-size: 28px; color: var(--white);
  }
  .contact-title span { color: var(--gold); }
  .contact-note {
    left: 58px; top: 928px; width: 226px;
    font-size: 9.6px; line-height: 12.4px; color: #e6e6e6;
  }
  .qr-spot {
    left: 298px; top: 884px; width: 70px; height: 70px;
    background: var(--white); border: 3px solid var(--accent-orange);
  }
  .phone-line {
    left: 58px; top: 982px; display: flex; align-items: center; gap: 8px;
    font-family: var(--serif); font-weight: 700; font-size: 40px; line-height: 44px; color: var(--white);
  }
  .phone-line svg { width: 24px; height: 24px; }
  .web-address {
    left: 58px; top: 1026px; font-size: 15px; line-height: 20px; letter-spacing: 5.5px; color: var(--white);
  }
  .base-strip { left: 0; top: 1060px; width: 380px; height: 17px; background: var(--accent-orange); }

  /* right column */
  .about {
    left: 408px; top: 470px; width: 330px;
    font-size: 12.6px; line-height: 16.2px; color: var(--text-dark);
  }
  .about strong { color: var(--accent-orange); font-weight: 600; }
  .services-panel { left: 380px; top: 643px; width: 380px; height: 434px; background: var(--accent-orange); }
  .services-pill {
    left: 408px; top: 626px; width: 324px; height: 42px; border-radius: 22px;
    background: var(--ink); border: 2px solid var(--accent-orange);
    display: flex; align-items: center; justify-content: center;
    font-family: var(--serif); font-weight: 700; font-size: 27px; color: var(--white);
  }
  .pill-pointer { left: 562px; top: 666px; width: 16px; height: 9px; }

  .service-photo { left: 408px; width: 135px; height: 113px; }
  .service-photo.windows { top: 691px; background: linear-gradient(180deg, #d7dde0 0%, #a9b4a0 40%, #6f6a62 75%, #4d4a46 100%); }
  .service-photo.doors { top: 815px; background: linear-gradient(90deg, #7d6a55 0%, #3d2a1f 30%, #2c1d15 55%, #3d2a1f 75%, #8a7660 100%); }
  .service-photo.siding { top: 939px; background: linear-gradient(180deg, #7fa3d6 0%, #c8d4e3 28%, #4d545a 55%, #3d4638 80%, #5d8a40 100%); }

  .service { left: 557px; width: 180px; color: var(--white); }
  .service h3 { font-size: 14px; line-height: 16px; font-weight: 700; margin-bottom: 4px; }
  .service p { font-size: 10.3px; line-height: 12.5px; color: #fff3e3; }
  .service.s1 { top: 688px; }
  .service.s2 { top: 812px; }
  .service.s3 { top: 937px; }
  .service-divider { left: 557px; width: 177px; height: 1px; background: rgba(255,255,255,0.45); }
</style>
</head>
<body>
<main class="flyer">
  <div class="abs hero-panel"></div>
  <div class="abs side-strip"></div>

  <div class="abs brand-block">
    <div class="brand-name">Granite Ridge<br>Remodeling</div>
  </div>
  <div class="abs brand-divider"></div>

  <h1 class="abs headline">Quality<br>Replacement<br>Windows, Doors<br><span class="highlight">and Siding at a<br>Fair Price!</span></h1>

  <div class="abs hero-photo" role="img" aria-label="Photo of a two-storey house with green board-and-batten siding and white-trimmed windows against a blue sky"></div>

  <div class="abs home-photo" role="img" aria-label="Photo of a grey-sided family home with a landscaped front lawn"></div>

  <h2 class="abs why-title">Why Choose Us?</h2>
  <div class="abs why-rule"></div>
  <ul class="abs benefits">
    <li><svg viewBox="0 0 20 20"><circle cx="10" cy="10" r="10" fill="#e3821c"/><path d="M5.5 10.3l3 3 6-6.2" fill="none" stroke="#fff" stroke-width="2.2" stroke-linecap="round" stroke-linejoin="round"/></svg>Affordable Pricing</li>
    <li><svg viewBox="0 0 20 20"><circle cx="10" cy="10" r="10" fill="#e3821c"/><path d="M5.5 10.3l3 3 6-6.2" fill="none" stroke="#fff" stroke-width="2.2" stroke-linecap="round" stroke-linejoin="round"/></svg>Free Consultations</li>
    <li><svg viewBox="0 0 20 20"><circle cx="10" cy="10" r="10" fill="#e3821c"/><path d="M5.5 10.3l3 3 6-6.2" fill="none" stroke="#fff" stroke-width="2.2" stroke-linecap="round" stroke-linejoin="round"/></svg>Experienced Professionals</li>
    <li><svg viewBox="0 0 20 20"><circle cx="10" cy="10" r="10" fill="#e3821c"/><path d="M5.5 10.3l3 3 6-6.2" fill="none" stroke="#fff" stroke-width="2.2" stroke-linecap="round" stroke-linejoin="round"/></svg>Fully Insured</li>
  </ul>

  <div class="abs contact-band"></div>
  <h2 class="abs contact-title">Get In <span>Touch</span></h2>
  <p class="abs contact-note">If you have any questions or would like to schedule an appointment for your free quote, scan the code or give us a call and we will get back to you as soon as possible.</p>
  <div class="abs qr-spot" role="img" aria-label="Space reserved for QR code"></div>
  <div class="abs phone-line">
    <svg viewBox="0 0 24 24"><circle cx="12" cy="12" r="12" fill="#e3821c"/><path d="M8.2 6.2c.5-.4 1.2-.3 1.5.2l1.2 1.9c.3.5.2 1.1-.2 1.4l-.8.6c.6 1.4 1.8 2.6 3.2 3.3l.6-.8c.3-.4 1-.5 1.4-.2l1.9 1.2c.5.3.6 1 .2 1.5l-.9 1c-.7.7-1.8.9-2.7.4-2.8-1.4-5-3.6-6.3-6.4-.4-.9-.2-2 .5-2.6z" fill="#fff"/></svg>
    860-412-9368
  </div>
  <div class="abs web-address">www.grr-vt.com</div>
  <div class="abs base-strip"></div>

  <p class="abs about"><strong>Granite Ridge Remodeling</strong> is a professional home improvement contractor based in Maple Hollow, VT. Our team of experts is dedicated to providing exceptional home improvement services to homeowners in Maple Hollow and surrounding areas. We specialize in replacement windows, doors and siding. We take pride in our work and always strive to exceed our clients' expectations.</p>

  <div class="abs services-panel"></div>
  <h2 class="abs services-pill">Our Services</h2>
  <svg class="abs pill-pointer" viewBox="0 0 16 9"><path d="M0 0h16L8 9z" fill="#0b0b0b"/></svg>

  <div class="abs service-photo windows" role="img" aria-label="Photo of a bright sunroom lined with replacement windows"></div>
  <div class="abs service s1">
    <h3>Replacement Window<br>Installation</h3>
    <p>Enhance energy efficiency, improve insulation, and elevate the appearance of your home with our expertly installed replacement windows.</p>
  </div>
  <div class="abs service-divider" style="top:805px"></div>

  <div class="abs service-photo doors" role="img" aria-label="Photo of a dark wooden front door with glass sidelights set in a stone wall"></div>
  <div class="abs service s2">
    <h3>Door Replacement<br>and Installation</h3>
    <p>Our skilled team will handle every aspect of the replacement and installation process, ensuring a seamless fit and lasting performance.</p>
  </div>
  <div class="abs service-divider" style="top:929px"></div>

  <div class="abs service-photo siding" role="img" aria-label="Photo of a house with new grey siding"></div>
  <div class="abs service s3">
    <h3>Siding Replacement<br>and Upgrades</h3>
    <p>Boost curb appeal, protect your home from the elements, and increase property value with our premium siding replacement and upgrade services.</p>
  </div>
</main>
</body>
</html>
```